Voltline Assemblies, Inc. Business Card

Voltline has three operating entities and I'm looking for a standard business card template that can be used for Voltline and the three operating entities that the logo just get swapped out, but has a very similar look and feel. Ultimately if someone had a business card from each, they assume the organizations are related because they all have the same look and feel.
Below are our websites and I will attached the logos for each entity:
https://www.voltlineassemblies.example/
https://www.brantoceramic.example/
https://www.omra-kfsd.example/
https://www.summitbreaker.example/

Target Market(s)

US Voltline

Industry/Entity Type

US Voltline

Contact Information for Business Card

Normal stuff

```html
<!DOCTYPE html>
<html lang="en">
<head>
<meta charset="utf-8">
<title>Voltline Assemblies, Inc. – Business Card</title>
<link rel="stylesheet" href="https://fonts.googleapis.com/css2?family=Montserrat:wght@600;700&family=Open+Sans:wght@400;500&display=swap">
<style>
  :root {
    --page: #cccccc;
    --card: #ffffff;
    --navy: #1f2f63;
    --red: #be1e2d;
    --red-deep: #8d1829;
    --red-mid: #a91c30;
    --ink: #333333;
    --map: #f0f0f0;
  }
  html, body {
    margin: 0;
    padding: 0;
    width: 1200px;
    height: 1200px;
    overflow: hidden;
    background: var(--page);
  }
  .canvas {
    position: relative;
    width: 1200px;
    height: 1200px;
  }
  .card {
    position: absolute;
    left: 177px;
    width: 784px;
    height: 449px;
    border-radius: 59px;
    background: var(--card);
    overflow: hidden;
  }
  .card--front { top: 144px; }
  .card--back { top: 633px; }
  .card__waves {
    position: absolute;
    inset: 0;
    width: 100%;
    height: 100%;
  }
  .brand {
    position: absolute;
    display: flex;
    align-items: center;
    font-family: "Montserrat", sans-serif;
    font-weight: 700;
    color: var(--navy);
    letter-spacing: 0.02em;
  }
  .brand__dot {
    border-radius: 50%;
    background: var(--navy);
    flex: none;
  }
  .card--front .brand {
    left: 45px;
    top: 25px;
    gap: 10px;
    font-size: 21px;
  }
  .card--front .brand__dot { width: 75px; height: 75px; }
  .holder-name {
    position: absolute;
    left: 55px;
    top: 170px;
    margin: 0;
    font-family: "Montserrat", sans-serif;
    font-weight: 700;
    font-size: 47px;
    color: var(--ink);
    letter-spacing: 0.01em;
  }
  .contact-list {
    position: absolute;
    left: 58px;
    top: 0;
    margin: 0;
    padding: 0;
    list-style: none;
    font-family: "Open Sans", sans-serif;
    font-size: 13.5px;
    font-weight: 500;
    color: var(--ink);
    line-height: 1.2;
  }
  .contact-list__item {
    position: absolute;
    left: 0;
    display: flex;
    align-items: center;
    gap: 9px;
    white-space: nowrap;
    transform: translateY(-50%);
  }
  .contact-list__icon {
    width: 31px;
    height: 31px;
    border-radius: 50%;
    background: var(--navy);
    display: flex;
    align-items: center;
    justify-content: center;
    flex: none;
  }
  .contact-list__icon svg { width: 17px; height: 17px; }
  .world-map {
    position: absolute;
    left: 90px;
    top: 65px;
    width: 515px;
    height: 314px;
    border-radius: 40px;
    background: radial-gradient(ellipse at center, var(--map) 55%, rgba(240,240,240,0) 100%);
  }
  .card--back .brand {
    left: 263px;
    top: 66px;
    transform: translateX(-50%);
    flex-direction: column;
    gap: 14px;
    font-size: 34px;
    line-height: 1.1;
    text-align: center;
    white-space: nowrap;
  }
  .card--back .brand__dot { width: 130px; height: 130px; }
</style>
</head>
<body>
<main class="canvas">

  <section class="card card--front" aria-label="Business card front">
    <svg class="card__waves" viewBox="0 0 1262 723" preserveAspectRatio="none" aria-hidden="true">
      <defs>
        <linearGradient id="waveRedFront" x1="0" y1="1" x2="1" y2="0">
          <stop offset="0" stop-color="#c41f30"/>
          <stop offset="1" stop-color="#8d1829"/>
        </linearGradient>
      </defs>
      <path d="M405 723 C700 620 950 300 1262 205 L1262 723 Z" fill="url(#waveRedFront)"/>
      <path d="M830 723 C930 480 1100 320 1262 250 L1262 723 Z" fill="var(--red-deep)"/>
      <path d="M860 723 C960 490 1110 340 1262 275 L1262 723 Z" fill="var(--red-mid)"/>
      <path d="M898 723 C1000 580 1120 470 1262 420 L1262 723 Z" fill="var(--navy)"/>
    </svg>

    <div class="brand">
      <span class="brand__dot"></span>
      <span class="brand__name">VOLTLINE ASSEMBLIES, INC.</span>
    </div>

    <h1 class="holder-name">YOUR NAME</h1>

    <ul class="contact-list">
      <li class="contact-list__item" style="top:272px">
        <span class="contact-list__icon">
          <svg viewBox="0 0 24 24" fill="none" stroke="#fff" stroke-width="2.2"><path d="M12 22s7-7 7-12a7 7 0 0 0-14 0c0 5 7 12 7 12z"/><circle cx="12" cy="10" r="2.5"/></svg>
        </span>
        <span>000 Street Name,<br>City Name, 0000 - ST</span>
      </li>
      <li class="contact-list__item" style="top:309px">
        <span class="contact-list__icon">
          <svg viewBox="0 0 24 24" fill="none" stroke="#fff" stroke-width="1.8"><circle cx="12" cy="12" r="9"/><ellipse cx="12" cy="12" rx="4" ry="9"/><path d="M3 12h18M5 7h14M5 17h14"/></svg>
        </span>
        <span>companywebsite.com</span>
      </li>
      <li class="contact-list__item" style="top:348px">
        <span class="contact-list__icon">
          <svg viewBox="0 0 24 24" fill="none" stroke="#fff" stroke-width="1.8"><rect x="3" y="6" width="18" height="12"/><path d="M3 6l9 7 9-7M3 18l7-6M21 18l-7-6"/></svg>
        </span>
        <span>youremail@company.com</span>
      </li>
      <li class="contact-list__item" style="top:389px">
        <span class="contact-list__icon">
          <svg viewBox="0 0 24 24" fill="#fff"><path d="M6.6 10.8a15 15 0 0 0 6.6 6.6l2.2-2.2a1 1 0 0 1 1-.25 11.4 11.4 0 0 0 3.6.57 1 1 0 0 1 1 1V20a1 1 0 0 1-1 1A17 17 0 0 1 3 4a1 1 0 0 1 1-1h3.5a1 1 0 0 1 1 1c0 1.25.2 2.45.57 3.6a1 1 0 0 1-.25 1z"/></svg>
        </span>
        <span>+000 12345 6789</span>
      </li>
    </ul>
  </section>

  <section class="card card--back" aria-label="Business card back">
    <div class="world-map" role="img" aria-label="Faint dotted world map backdrop"></div>

    <svg class="card__waves" viewBox="0 0 1262 723" preserveAspectRatio="none" aria-hidden="true">
      <defs>
        <linearGradient id="waveRedBack" x1="0" y1="1" x2="1" y2="0">
          <stop offset="0" stop-color="#c41f30"/>
          <stop offset="1" stop-color="#8d1829"/>
        </linearGradient>
      </defs>
      <path d="M405 723 C700 620 950 300 1262 205 L1262 723 Z" fill="url(#waveRedBack)"/>
      <path d="M830 723 C930 480 1100 320 1262 250 L1262 723 Z" fill="var(--red-deep)"/>
      <path d="M860 723 C960 490 1110 340 1262 275 L1262 723 Z" fill="var(--red-mid)"/>
      <path d="M898 723 C1000 580 1120 470 1262 420 L1262 723 Z" fill="var(--navy)"/>
    </svg>

    <div class="brand">
      <span class="brand__dot"></span>
      <span class="brand__name">VOLTLINE<br>ASSEMBLIES, INC.</span>
    </div>
  </section>

</main>
</body>
</html>
```